life insurance quote website design for lavoiesereine.ca

the web site lavoiesereine.ca need a design. we dont like the actuel one but we are open at all new suggestion. visit us at lavoiesereine.ca and you will understand. the principal concurant is devisrapidecouvert.ca, tarifoulot.ca, coutprotegebien.ca. We are a life insurance quote site. we found best price available in the canadien industrie. We absolutly want a design with our form in the front page on the top right side like our concurance, we use wordpress at this time. we want to be able to switch language. and to have a logic form. we want to be able to change the color for each type of insurance quote page.we also need a blog in it to post news. and the site will be SEO accurate.

Target Market(s)

Get client fill the quote form

Industry/Entity Type

Insurance

Number of Pages Required

3 page

Font styles to use
Sans Serif

Requirements
Must have
• logic form on the top right first page
• page template for product info stuff, contact, and who we are, blog
• French site
• custum color
Nice to have
• Wordpress design will be appréciate
• switch language english/french

```html
<!DOCTYPE html>
<html lang="en">
<head>
<meta charset="utf-8">
<title>La Voie Sereine – Life Insurance Quotes</title>
<link rel="stylesheet" href="https://fonts.googleapis.com/css2?family=Open+Sans:ital,wght@0,400;0,600;0,700;0,800;1,400;1,600&display=swap">
<style>
:root{
  --red:#e8121b;
  --navy:#1d3f73;
  --blue:#1f4f94;
  --panel:#234e8e;
  --ink:#1b1b1b;
  --text:#666;
  --light:#f1f1f1;
  --line:#dcdcdc;
  --footer:#2a2a2a;
  --footer-deep:#1f1f1f;
  --cyan:#2fb0d9;
  --gold:#d9a033;
  --green:#6cbf4a;
  --pink:#e8657e;
}
*{box-sizing:border-box;margin:0;padding:0}
html,body{width:1200px;height:2462px;overflow:hidden;background:#fff}
body{font-family:"Open Sans",Arial,sans-serif;color:var(--ink)}
.canvas{position:relative;width:1200px;height:2462px;overflow:hidden}
.abs{position:absolute}

/* header */
.topline{left:0;top:0;width:1200px;height:5px;background:var(--red)}
.brand{left:92px;top:40px;font-size:26px;font-weight:800;color:var(--red);display:flex;align-items:center;gap:10px;letter-spacing:.3px}
.brand .dot{width:22px;height:22px;background:var(--red);border-radius:50%}
.utility{top:18px;font-size:13px;color:#333;display:flex;align-items:center;gap:8px}
.flag{width:18px;height:12px;display:inline-block}
.round-icon{width:30px;height:30px;border:2px solid var(--red);border-radius:50%;display:flex;align-items:center;justify-content:center}
.nav{top:62px;left:0;font-size:13px;font-weight:700;color:#222}
.nav span{position:absolute;white-space:nowrap}

/* hero */
.hero{left:0;top:94px;width:1200px;height:467px;background:linear-gradient(180deg,#8fc2e8 0%,#cfe4f3 45%,#a9c56e 72%,#6f9a3a 100%)}
.hero-text{left:98px;color:#fff;font-weight:800;text-shadow:0 2px 4px rgba(0,0,0,.35)}
.hero-arrow{top:310px}
.quote{left:699px;top:94px;width:401px;height:467px;background:rgba(35,78,142,.93);color:#fff}
.quote h2{position:absolute;top:10px;width:100%;text-align:center;font-size:21px;font-weight:700}
.quote .group{position:absolute;left:23px;font-size:13px;font-weight:700}
.quote .label{position:absolute;left:23px;font-size:12px}
.quote .field{position:absolute;left:151px;width:225px;height:28px;background:#fff}
.quote .select::after{content:"";position:absolute;right:0;top:0;width:32px;height:28px;background:#ddd}
.quote .select::before{content:"";position:absolute;right:11px;top:11px;border:5px solid transparent;border-top-color:#555;z-index:1}
.box{display:inline-block;width:15px;height:15px;background:#fff;vertical-align:middle;margin-right:8px}
.send{position:absolute;left:23px;top:417px;width:360px;height:37px;background:var(--red);font-size:15px;font-weight:700;text-align:center;line-height:37px;border-radius:2px}

/* section titles */
.section-title{width:1200px;text-align:center;font-size:22px;font-weight:800;color:var(--ink)}
.section-title em{font-style:normal;color:var(--navy)}

/* welcome */
.mission{left:200px;top:644px;width:800px;text-align:center;font-size:12px;line-height:22px;color:var(--text)}
.service{width:230px;text-align:center}
.service .badge{display:block;margin:0 auto;width:104px;height:104px;border-radius:50%;border:4px solid currentColor;position:relative;margin-top:10px}
.service .badge::after{content:"";position:absolute;left:30px;top:30px;width:36px;height:36px;border-radius:50%;background:currentColor;opacity:.85}
.service h3{margin-top:28px;font-size:15px;font-weight:700}
.service p{margin:12px auto 0;width:210px;font-size:12px;line-height:23px;color:var(--text)}
.service .bid{margin-top:12px;font-size:12px;font-weight:800;color:var(--red)}

/* products */
.products-band{left:0;top:1026px;width:1200px;height:435px;background:var(--light)}
.card{width:235px;height:300px;background:#fff;border:1px solid var(--line);padding:4px;overflow:hidden}
.card .photo{height:131px}
.card h4{margin:16px 7px 0;font-size:14px;font-weight:700}
.card .lead{margin:6px 7px 0;font-size:11.5px;line-height:19px;font-style:italic;font-weight:600;color:#333}
.card .body{margin:9px 7px 0;font-size:12px;line-height:20px;color:var(--text)}
.card .corner{position:absolute;right:0;bottom:0;width:0;height:0;border-left:44px solid transparent;border-bottom:44px solid var(--red)}
.card .plus{position:absolute;right:6px;bottom:4px;color:#fff;font-weight:700;font-size:16px}

/* blog */
.post{width:235px}
.post .photo{position:relative;height:145px;border:4px solid #fff;box-shadow:0 0 0 1px var(--line)}
.post .date{position:absolute;right:0;bottom:0;background:rgba(0,0,0,.7);color:#fff;font-size:11px;font-weight:600;padding:3px 6px}
.post h4{margin-top:22px;font-size:14px;font-weight:700;line-height:21px}
.post p{margin-top:8px;font-size:12px;line-height:21px;color:var(--text)}
.post .more{margin-top:12px;font-size:11.5px;font-weight:700;color:var(--red)}

/* offices */
.offices{left:0;top:1876px;width:1200px;height:283px;background:linear-gradient(180deg,#5a9fd8 0%,#a9d0ee 55%,#cfe6c2 85%,#7dbb4a 100%)}
.offices-family{left:739px;top:0;width:461px;height:283px;background:linear-gradient(135deg,#e9c9a6 0%,#c79a72 55%,#a2d06e 100%)}
.offices h2{position:absolute;left:102px;top:36px;font-size:22px;font-weight:800;color:var(--navy)}
.offices h2 em{font-style:normal;color:var(--blue)}
.city{position:absolute;font-size:12.5px;font-weight:700;color:#222;display:flex;align-items:center;gap:9px}
.tick{width:15px;height:15px;border-radius:50%;background:var(--red);display:flex;align-items:center;justify-content:center}

/* footer */
.footer{left:0;top:2159px;width:1200px;height:254px;background:var(--footer);color:#ddd}
.footer-brand{position:absolute;left:70px;top:108px;font-size:18px;font-weight:800;color:var(--red)}
.col-sep{position:absolute;top:0;width:1px;height:254px;background:#3a3a3a}
.footer h5{position:absolute;top:32px;font-size:15px;font-weight:700;color:#fff}
.footer .small{position:absolute;font-size:12px;color:#ccc;line-height:21px}
.email-input{position:absolute;left:540px;top:121px;width:263px;height:34px;background:#fff;font-size:12px;color:#888;padding:9px 13px}
.subscribe{position:absolute;left:540px;top:171px;width:101px;height:36px;border:2px solid #fff;border-radius:4px;color:#fff;font-size:13px;font-weight:700;text-align:center;line-height:32px}
.contact-row{position:absolute;left:865px;display:flex;align-items:center;gap:14px;font-size:12px;color:#ccc}
.bottom{left:0;top:2413px;width:1200px;height:49px;background:var(--footer-deep);color:#ccc;font-size:12px}
.social{position:absolute;top:12px;width:27px;height:27px;border:1px solid #ccc;border-radius:50%}
</style>
</head>
<body>
<div class="canvas">

  <div class="abs topline"></div>
  <div class="abs brand"><span class="dot"></span>La Voie Sereine</div>

  <div class="abs utility" style="left:547px">
    <svg class="flag" viewBox="0 0 18 12"><rect width="18" height="12" fill="#fff"/><rect width="5" height="12" fill="#e8121b"/><rect x="13" width="5" height="12" fill="#e8121b"/><rect x="7.5" y="4" width="3" height="4" fill="#e8121b"/></svg>English
  </div>
  <div class="abs utility" style="left:630px">
    <svg class="flag" viewBox="0 0 18 12"><rect width="18" height="12" fill="#1f4f94"/><rect x="8" width="2" height="12" fill="#fff"/><rect y="5" width="18" height="2" fill="#fff"/></svg>French
  </div>
  <div class="abs utility" style="left:708px;top:13px">
    <span class="round-icon"><svg width="14" height="10" viewBox="0 0 14 10"><rect x=".5" y=".5" width="13" height="9" fill="none" stroke="#e8121b"/><path d="M.5 .5 7 6 13.5 .5" fill="none" stroke="#e8121b"/></svg></span>
    <span style="margin-left:6px">contact@lavoiesereine.ca</span>
  </div>
  <div class="abs utility" style="left:955px;top:13px">
    <span class="round-icon"><svg width="14" height="14" viewBox="0 0 14 14"><path d="M3 1l2.5 3-1.5 1.5c.8 1.8 2.2 3.2 4 4L9.5 8 13 10.5 11.5 13C6 13 1 8 1 2.5z" fill="#e8121b"/></svg></span>
    <span style="margin-left:8px">1-855-555-0142</span>
  </div>

  <nav class="abs nav">
    <span style="left:556px;color:var(--red)">HOME</span>
    <span style="left:627px">PRODUCTS</span>
    <span style="left:734px">SUBMISSION</span>
    <span style="left:845px">WHO ARE WE?</span>
    <span style="left:970px">CONTACT US</span>
    <span style="left:1084px"><svg width="13" height="13" viewBox="0 0 13 13"><circle cx="5.5" cy="5.5" r="4" fill="none" stroke="#222" stroke-width="2"/><path d="M8.5 8.5 12 12" stroke="#222" stroke-width="2"/></svg></span>
  </nav>

  <div class="abs hero" role="img" aria-label="Photo of a smiling family outdoors in a sunny green field, father carrying a child on his shoulders"></div>
  <div class="abs hero-text" style="top:288px;font-size:27px">THE ASSURANCE OF</div>
  <div class="abs hero-text" style="top:322px;font-size:39px">GETTING THE BEST PRICE</div>
  <svg class="abs hero-arrow" style="left:52px" width="18" height="32" viewBox="0 0 18 32"><path d="M16 2 2 16l14 14" fill="none" stroke="#fff" stroke-width="3"/></svg>
  <svg class="abs hero-arrow" style="left:1147px" width="18" height="32" viewBox="0 0 18 32"><path d="M2 2l14 14L2 30" fill="none" stroke="#fff" stroke-width="3"/></svg>

  <form class="abs quote">
    <h2>QUOTE REQUEST</h2>
    <div class="group" style="top:50px">Product</div>
    <div class="label" style="top:78px">Type of Insurance :</div>
    <div class="field select" style="top:72px"></div>
    <div class="group" style="top:110px">Applicant</div>
    <div class="label" style="top:143px">Full Name * :</div>
    <div class="field" style="top:136px"></div>
    <div class="label" style="top:179px">Cities * :</div>
    <div class="field" style="top:172px"></div>
    <div class="label" style="top:215px">Email * :</div>
    <div class="field" style="top:208px"></div>
    <div class="label" style="top:250px">Phone * :</div>
    <div class="field" style="top:243px"></div>
    <div class="label" style="top:287px">Age * :</div>
    <div class="field" style="top:280px"></div>
    <div class="label" style="top:318px">Gender * :</div>
    <div class="label" style="left:151px;top:316px"><span class="box"></span>Man</div>
    <div class="label" style="left:218px;top:316px"><span class="box"></span>Wife</div>
    <div class="group" style="top:342px">Co-Applicant</div>
    <div class="label" style="top:372px"><span class="box"></span>Add a co-applicant</div>
    <div class="label" style="left:172px;top:370px;width:215px;line-height:16px;padding-left:23px;text-indent:-23px"><span class="box"></span>I have read and accept the use and privacy policy of **</div>
    <div class="send">SEND</div>
  </form>

  <h1 class="abs section-title" style="top:597px">WELCOME TO <em>LA VOIE SEREINE</em></h1>
  <p class="abs mission">Our mission is to help our customers find the insurance that best meets their needs taking into account the best possible price. The consultant team always realize the financial needs analysis to determine the best choice of product.</p>

  <div class="abs service" style="left:89px;top:718px">
    <span class="badge" style="color:var(--cyan)"></span>
    <h3>ASSURANCE VIE</h3>
    <p>A fast, free and confidential. Fill the life insurance quote form and you will enjoy your experience with us</p>
    <div class="bid">BIDDING</div>
  </div>
  <div class="abs service" style="left:353px;top:718px">
    <span class="badge" style="color:var(--gold)"></span>
    <h3>SALAIRE</h3>
    <p>A fast, free and confidential. Fill the life insurance quote form and you will enjoy your experience with us</p>
    <div class="bid">BIDDING</div>
  </div>
  <div class="abs service" style="left:614px;top:718px">
    <span class="badge" style="color:var(--green)"></span>
    <h3>HYPOTHECAIRE</h3>
    <p>A fast, free and confidential. Fill the life insurance quote form and you will enjoy your experience with us</p>
    <div class="bid">BIDDING</div>
  </div>
  <div class="abs service" style="left:877px;top:718px">
    <span class="badge" style="color:var(--pink)"></span>
    <h3>MALADIES GRAVES</h3>
    <p>A fast, free and confidential. Fill the life insurance quote form and you will enjoy your experience with us</p>
    <div class="bid">BIDDING</div>
  </div>

  <div class="abs products-band"></div>
  <h2 class="abs section-title" style="top:1055px">OUR <em>PRODUCTS</em></h2>

  <article class="abs card" style="left:98px;top:1115px">
    <div class="photo" role="img" aria-label="Photo of a couple reviewing paperwork with an advisor at a desk" style="background:linear-gradient(135deg,#9fb6c9,#4c6d8e)"></div>
    <h4>DISABILITY INSURANCE</h4>
    <p class="lead">Protect themselves in case of disability with the disability insurance</p>
    <p class="body">Salary / disability insurance is a useful protection, which will save you many troubles.</p>
    <span class="corner"></span><span class="plus">+</span>
  </article>
  <article class="abs card" style="left:353px;top:1115px">
    <div class="photo" role="img" aria-label="Photo of a smiling family with a young child outdoors" style="background:linear-gradient(135deg,#8cbf5a,#d6b08a)"></div>
    <h4>LIFE INSURANCE</h4>
    <p class="lead">To Protect your loved ones</p>
    <p class="body">A life insurance policy allows you to not worry about what will happen to your family in case of your death.</p>
    <span class="corner"></span><span class="plus">+</span>
  </article>
  <article class="abs card" style="left:607px;top:1115px">
    <div class="photo" role="img" aria-label="Photo of a handshake over a small model house" style="background:linear-gradient(135deg,#e7e7e7,#b94a4a)"></div>
    <h4>MORTGAGE INSURANCE</h4>
    <p class="lead">The importance of protecting your investments with mortgage insurance</p>
    <p class="body">Do you recognize yourself in the statement? "I want to protect myself and my family. Is there ..</p>
    <span class="corner"></span><span class="plus">+</span>
  </article>
  <article class="abs card" style="left:865px;top:1115px">
    <div class="photo" role="img" aria-label="Photo of a senior couple exercising on the grass in a park" style="background:linear-gradient(180deg,#b8d4a0,#5f9a3c)"></div>
    <h4>SERIOUS DISEASES</h4>
    <p class="lead">Benefit from a serious illness insurance that protects against any eventuality</p>
    <p class="body">Serious diseases such as cancer or a stroke (CVA) are the tragic events. The consequences caused ..</p>
    <span class="corner"></span><span class="plus">+</span>
  </article>

  <h2 class="abs section-title" style="top:1492px">OUR <em>BLOG</em></h2>

  <article class="abs post" style="left:98px;top:1548px">
    <div class="photo" role="img" aria-label="Photo of an advisor meeting a couple at a table" style="background:linear-gradient(135deg,#c9a88a,#7a5c48)"><span class="date">05/04/2016</span></div>
    <h4>HOW TO PROCEED?</h4>
    <p>Simply fill in the insurance quote online form above, clicking on the insurance category that fits your needs.</p>
    <div class="more">READ MORE &gt;&gt;</div>
  </article>
  <article class="abs post" style="left:353px;top:1548px">
    <div class="photo" role="img" aria-label="Photo of a financial advisor with a couple in an office" style="background:linear-gradient(135deg,#e4e4e4,#9a7a68)"><span class="date">05/04/2016</span></div>
    <h4>COMPETENT FINANCIAL<br>ADVISORS SECURITY</h4>
    <p>Team La Voie Sereine offers an innovative service in the field,..</p>
    <div class="more">READ MORE &gt;&gt;</div>
  </article>
  <article class="abs post" style="left:607px;top:1548px">
    <div class="photo" role="img" aria-label="Photo of a senior woman discussing documents with an advisor" style="background:linear-gradient(135deg,#d9b896,#8c5a3e)"><span class="date">05/04/2016</span></div>
    <h4>THE IMPORTANCE OF<br>NOT OVERPAYING</h4>
    <p>Disbursing monthly or annually money for insurance is a considerable expense.</p>
    <div class="more">READ MORE &gt;&gt;</div>
  </article>
  <article class="abs post" style="left:865px;top:1548px">
    <div class="photo" role="img" aria-label="Photo of a businessman holding a savings sign" style="background:linear-gradient(135deg,#2f8fcf,#1c4e7a)"><span class="date">05/04/2016</span></div>
    <h4>INSURANCE: ? HOW TO FIND</h4>
    <p>The life insurance market premium may seem complex at first. Indeed, insurers offer a variety of products ..</p>
    <div class="more">READ MORE &gt;&gt;</div>
  </article>

  <section class="abs offices" role="img" aria-label="Bright blue sky with clouds over green grass">
    <div class="abs offices-family" role="img" aria-label="Photo of a smiling family of four lying on the grass"></div>
    <h2>OUR <em>OFFICES</em></h2>
    <div class="city" style="left:102px;top:92px"><span class="tick"><svg width="9" height="9" viewBox="0 0 9 9"><path d="m1 4.5 2.5 2.5L8 2" fill="none" stroke="#fff" stroke-width="2"/></svg></span>MONTREAL</div>
    <div class="city" style="left:102px;top:128px"><span class="tick"><svg width="9" height="9" viewBox="0 0 9 9"><path d="m1 4.5 2.5 2.5L8 2" fill="none" stroke="#fff" stroke-width="2"/></svg></span>QUEBEC</div>
    <div class="city" style="left:102px;top:164px"><span class="tick"><svg width="9" height="9" viewBox="0 0 9 9"><path d="m1 4.5 2.5 2.5L8 2" fill="none" stroke="#fff" stroke-width="2"/></svg></span>SHERBROOKE</div>
    <div class="city" style="left:102px;top:200px"><span class="tick"><svg width="9" height="9" viewBox="0 0 9 9"><path d="m1 4.5 2.5 2.5L8 2" fill="none" stroke="#fff" stroke-width="2"/></svg></span>GRANBY</div>
    <div class="city" style="left:102px;top:236px"><span class="tick"><svg width="9" height="9" viewBox="0 0 9 9"><path d="m1 4.5 2.5 2.5L8 2" fill="none" stroke="#fff" stroke-width="2"/></svg></span>BEAUCE</div>

    <div class="city" style="left:238px;top:92px"><span class="tick"><svg width="9" height="9" viewBox="0 0 9 9"><path d="m1 4.5 2.5 2.5L8 2" fill="none" stroke="#fff" stroke-width="2"/></svg></span>THREE RIVÈRES</div>
    <div class="city" style="left:238px;top:128px"><span class="tick"><svg width="9" height="9" viewBox="0 0 9 9"><path d="m1 4.5 2.5 2.5L8 2" fill="none" stroke="#fff" stroke-width="2"/></svg></span>PIEDMONT</div>
    <div class="city" style="left:238px;top:164px"><span class="tick"><svg width="9" height="9" viewBox="0 0 9 9"><path d="m1 4.5 2.5 2.5L8 2" fill="none" stroke="#fff" stroke-width="2"/></svg></span>SAGUENAY</div>
    <div class="city" style="left:238px;top:200px"><span class="tick"><svg width="9" height="9" viewBox="0 0 9 9"><path d="m1 4.5 2.5 2.5L8 2" fill="none" stroke="#fff" stroke-width="2"/></svg></span>GOODS</div>
    <div class="city" style="left:238px;top:236px"><span class="tick"><svg width="9" height="9" viewBox="0 0 9 9"><path d="m1 4.5 2.5 2.5L8 2" fill="none" stroke="#fff" stroke-width="2"/></svg></span>CHICOUTIMI</div>

    <div class="city" style="left:384px;top:92px"><span class="tick"><svg width="9" height="9" viewBox="0 0 9 9"><path d="m1 4.5 2.5 2.5L8 2" fill="none" stroke="#fff" stroke-width="2"/></svg></span>SEPT-ILES</div>
    <div class="city" style="left:384px;top:128px"><span class="tick"><svg width="9" height="9" viewBox="0 0 9 9"><path d="m1 4.5 2.5 2.5L8 2" fill="none" stroke="#fff" stroke-width="2"/></svg></span>ROUYN-NORANDA</div>
    <div class="city" style="left:384px;top:164px"><span class="tick"><svg width="9" height="9" viewBox="0 0 9 9"><path d="m1 4.5 2.5 2.5L8 2" fill="none" stroke="#fff" stroke-width="2"/></svg></span>VAL D'OR</div>
    <div class="city" style="left:384px;top:200px"><span class="tick"><svg width="9" height="9" viewBox="0 0 9 9"><path d="m1 4.5 2.5 2.5L8 2" fill="none" stroke="#fff" stroke-width="2"/></svg></span>GATINEAU</div>
    <div class="city" style="left:384px;top:236px"><span class="tick"><svg width="9" height="9" viewBox="0 0 9 9"><path d="m1 4.5 2.5 2.5L8 2" fill="none" stroke="#fff" stroke-width="2"/></svg></span>VICTORIAVILLE</div>

    <div class="city" style="left:546px;top:92px"><span class="tick"><svg width="9" height="9" viewBox="0 0 9 9"><path d="m1 4.5 2.5 2.5L8 2" fill="none" stroke="#fff" stroke-width="2"/></svg></span>AMQUI</div>
    <div class="city" style="left:546px;top:128px"><span class="tick"><svg width="9" height="9" viewBox="0 0 9 9"><path d="m1 4.5 2.5 2.5L8 2" fill="none" stroke="#fff" stroke-width="2"/></svg></span>WOLF RIVER</div>
    <div class="city" style="left:546px;top:164px"><span class="tick"><svg width="9" height="9" viewBox="0 0 9 9"><path d="m1 4.5 2.5 2.5L8 2" fill="none" stroke="#fff" stroke-width="2"/></svg></span>CHATEAUGUAY</div>
    <div class="city" style="left:546px;top:200px"><span class="tick"><svg width="9" height="9" viewBox="0 0 9 9"><path d="m1 4.5 2.5 2.5L8 2" fill="none" stroke="#fff" stroke-width="2"/></svg></span>LA PRAIRIE</div>
  </section>

  <footer class="abs footer">
    <div class="footer-brand">La Voie Sereine</div>
    <span class="col-sep" style="left:245px"></span>
    <span class="col-sep" style="left:505px"></span>
    <span class="col-sep" style="left:838px"></span>

    <h5 style="left:279px">Hours of Operation</h5>
    <div class="small" style="left:279px;top:75px">Monday to Friday:</div>
    <div class="small" style="left:390px;top:75px">7am to 21hrs</div>
    <div class="small" style="left:279px;top:109px">Sunday:</div>
    <div class="small" style="left:390px;top:109px">10hrs to 15hrs</div>

    <h5 style="left:540px">Newsletter</h5>
    <div class="small" style="left:540px;top:68px;width:210px">Register your email address to get information about us</div>
    <div class="email-input">Email Address</div>
    <div class="subscribe">SUBSCRIBE</div>

    <h5 style="left:865px">Contact Us</h5>
    <div class="contact-row" style="top:74px"><svg width="10" height="14" viewBox="0 0 10 14"><path d="M5 0a5 5 0 0 1 5 5c0 4-5 9-5 9S0 9 0 5a5 5 0 0 1 5-5z" fill="#ccc"/><circle cx="5" cy="5" r="2" fill="#2a2a2a"/></svg>48 Rue des Érables, La Prairie, QC, J5R 0A0</div>
    <div class="contact-row" style="top:120px"><svg width="12" height="12" viewBox="0 0 14 14"><path d="M3 1l2.5 3-1.5 1.5c.8 1.8 2.2 3.2 4 4L9.5 8 13 10.5 11.5 13C6 13 1 8 1 2.5z" fill="#ccc"/></svg>1-855-555-0142</div>
    <div class="contact-row" style="top:166px"><svg width="13" height="10" viewBox="0 0 14 10"><rect width="14" height="10" fill="#ccc"/><path d="M0 0 7 6 14 0" fill="none" stroke="#2a2a2a"/></svg>contact@lavoiesereine.ca</div>
  </footer>

  <div class="abs bottom">
    <span class="abs" style="left:98px;top:15px">Copyrights ©2016, La Voie Sereine. All rights reserved.</span>
    <span class="social" style="left:970px"></span>
    <span class="social" style="left:1005px"></span>
    <span class="social" style="left:1040px"></span>
    <span class="social" style="left:1075px"></span>
  </div>

</div>
</body>
</html>
```